Brightlane Pixel Collective Website

I need my website redesigned to look very modern with the latest services. Check out my old website for information: www.brightlanepixelcollective.com

You can use the same site menu links

It doesn't need to have the Recent News section

Please use the yellow, black and grey color scheme
Updates

This project is now payment guaranteed. Lets see what everyone can do!

Target Market(s)

25-50 years in range. Small Business Owners

Industry/Entity Type

Group

Requirements
Must have
• Logo and similar color scheme to current website
• Modern, Modern, Modern! I want a very fresh and modern look
Should not have
• Boring Look

```html
<!DOCTYPE html>
<html lang="en">
<head>
<meta charset="utf-8">
<title>Brightlane Pixel Collective</title>
<link href="https://fonts.googleapis.com/css2?family=Open+Sans:wght@300;400;600;700&display=swap" rel="stylesheet">
<style>
:root{
  --yellow:#ffc400;
  --yellow-deep:#ffb000;
  --yellow-light:#ffe000;
  --black:#000;
  --grey-band:#2b2b2b;
  --text:#e6e6e6;
  --white:#fff;
}
*{margin:0;padding:0;box-sizing:border-box}
html,body{width:934px;height:1200px;overflow:hidden;background:var(--black)}
body{position:relative;font-family:'Open Sans',sans-serif;color:var(--text)}
.abs{position:absolute}
a{color:inherit;text-decoration:none}

/* header */
.header{left:0;top:0;width:934px;height:73px;background:var(--black)}
.brand{left:155px;top:10px;width:150px;text-align:center}
.brand-mark{width:26px;height:26px;background:var(--yellow);margin:0 auto 6px}
.brand-name{font-size:9px;color:#d8d8d8;letter-spacing:.2px;white-space:nowrap}
.contact-line{left:389px;top:11px;font-size:10.5px;font-weight:700;color:var(--white);white-space:nowrap}
.contact-line span{margin:0 6px;font-weight:400}
.estimate{left:648px;top:9px;width:132px;height:21px;background:var(--yellow);color:var(--white);font-size:9.5px;font-weight:700;text-align:center;line-height:21px}
.nav{left:360px;top:40px;display:flex;height:33px}
.nav a{font-size:11px;color:var(--white);padding:0 12px;line-height:40px;height:33px}
.nav a.active{background:var(--yellow);color:#222;border-radius:4px 4px 0 0;padding:0 14px;line-height:40px}

/* hero */
.hero{left:0;top:73px;width:934px;height:302px;background:radial-gradient(ellipse at 50% 40%,var(--yellow-light),var(--yellow-deep) 75%)}
.hero-title{left:170px;top:124px;font-size:26px;font-weight:300;color:#222}
.hero-art{left:395px;top:77px;width:360px;height:180px;background:linear-gradient(90deg,#b8302a,#f4f4f4 35%,#f4f4f4 75%,#d8d8d8);border-radius:2px}
.arrow{top:133px;width:38px;height:38px;border-radius:50%;background:rgba(255,255,255,.45)}
.arrow.prev{left:93px}.arrow.next{left:801px}

/* features */
.feature{top:414px;width:200px;height:330px}
.feature h2{font-size:13px;font-weight:600;color:var(--yellow);margin-bottom:9px}
.feature .pic{width:200px;height:115px;background:linear-gradient(#fafafa,#e4e4e4)}
.feature h3{font-size:9.6px;font-weight:700;color:var(--white);line-height:16px;margin-top:10px;height:38px}
.feature p{font-size:9.5px;line-height:16px;color:#ddd;margin-top:6px;width:206px;letter-spacing:-.15px}
.btn{position:absolute;left:0;top:306px;background:var(--yellow);color:#222;font-size:9.5px;padding:0 10px;height:21px;line-height:21px;border-radius:3px}

/* recent works */
.works{left:0;top:756px;width:934px;height:226px;background:var(--grey-band)}
.works h2{position:absolute;left:0;width:934px;top:12px;text-align:center;font-size:12.5px;font-weight:600;color:var(--yellow)}
.work{top:45px;width:160px;text-align:center}
.work .thumb{margin:0 auto;height:86px}
.work h4{font-size:9.5px;font-weight:600;color:var(--white);margin-top:30px}
.work p{font-size:9.5px;line-height:16px;color:#ddd}
.work a{font-size:9.5px;color:var(--yellow)}

/* footer */
.footcol{top:1003px;font-size:8px;color:var(--white)}
.footcol h5{font-size:8px;font-weight:700;margin-bottom:30px}
.footcol li{list-style:none;line-height:20px;color:#ddd}
.widget{left:635px;top:1000px;width:145px;height:106px;background:var(--white);border:1px solid #ccc}
.widget .top{margin:3px;height:37px;background:var(--black);display:flex;align-items:center;padding-left:10px;gap:5px}
.widget .top i{width:12px;height:12px;background:var(--yellow);display:block}
.widget .top b{font-size:5.5px;font-weight:400;color:#ccc}
.widget .like{font-size:5.5px;color:#333;margin:5px 9px}
.faces{display:flex;gap:3px;margin:0 9px}
.faces i{width:22px;height:22px;background:#b9a99a;display:block}
.widget .plug{font-size:5px;color:#777;margin:4px 9px}
.social{left:718px;top:1121px;display:flex;gap:3px}
.social i{width:19px;height:19px;border-radius:3px;display:block}
.foot-brand{left:155px;top:1143px;width:120px;text-align:center}
.foot-brand .brand-mark{width:20px;height:20px;margin-bottom:5px}
.foot-brand .brand-name{font-size:7px}
.legal{right:154px;top:1154px;font-size:7.5px;color:#ddd;white-space:nowrap}
.legal .city{margin-right:14px}
.copy{right:154px;top:1175px;font-size:7.5px;color:var(--white)}
</style>
</head>
<body>

<header class="abs header">
  <div class="abs brand"><div class="brand-mark"></div><div class="brand-name">BRIGHTLANE PIXEL COLLECTIVE</div></div>
  <div class="abs contact-line">Local: 612-555-0142 <span>|</span>Toll Free: 1-866-555-0187</div>
  <a class="abs estimate" href="#">Request Free Estimate</a>
  <nav class="abs nav">
    <a class="active" href="#">Home</a><a href="#">Web Design</a><a href="#">Search Engine Marketing</a><a href="#">Social Media</a><a href="#">Contact</a>
  </nav>
</header>

<section class="abs hero">
  <div class="abs arrow prev"><svg width="38" height="38"><path d="M22 11 L14 19 L22 27" stroke="#fff" stroke-width="4" fill="none" stroke-linecap="round" stroke-linejoin="round"/></svg></div>
  <h1 class="abs hero-title">Web Desigining</h1>
  <div class="abs hero-art" role="img" aria-label="Fanned stack of website screenshots"></div>
  <div class="abs arrow next"><svg width="38" height="38"><path d="M16 11 L24 19 L16 27" stroke="#fff" stroke-width="4" fill="none" stroke-linecap="round" stroke-linejoin="round"/></svg></div>
</section>

<article class="abs feature" style="left:153px">
  <h2>Our Mission</h2>
  <div class="pic" role="img" aria-label="Business team standing together"></div>
  <h3>Brightlane Pixel Collective will get you noticed</h3>
  <p>We are an award winning web design &amp; internet marketing company located in Minneapolis. As a Minneapolis Web Design company, we create web sites to what our clients want and that's found in our marketing. Here at Brightlane Pixel Collective</p>
  <a class="btn" href="#">Read More</a>
</article>
<article class="abs feature" style="left:367px">
  <h2>Internet Marketing</h2>
  <div class="pic" role="img" aria-label="Desktop computer and tablet with a green arrow"></div>
  <h3>Home of the "Pay for Performance" Guarantee</h3>
  <p>You've invested countless hours and a large sum of money to build your online presence, why waste the investment by not marketing it? Even if you've built it to give your current customers information about your business... don't you want more local</p>
  <a class="btn" href="#">Read More</a>
</article>
<article class="abs feature" style="left:581px">
  <h2>Website Design</h2>
  <div class="pic" role="img" aria-label="Stack of browser windows"></div>
  <h3>A Rewarding Experience</h3>
  <p>Welcome to Brightlane Pixel Collective. We are very excited and proud to help you achieve the internet solution that you need. We have an experienced team of web designers, developers, graphic designers, SEO specialist, social networking professionals</p>
  <a class="btn" href="#">Read More</a>
</article>

<section class="abs works">
  <h2>Recent Works</h2>
  <div class="abs work" style="left:146px"><div class="thumb" role="img" aria-label="Outdoor fair website screenshot" style="width:130px;background:linear-gradient(#c2521c,#8a2a12)"></div><h4>Maple Ridge Fire Department</h4><p>Web Design</p><a href="#">www.mapleridgefire.com</a></div>
  <div class="abs work" style="left:305px"><div class="thumb" role="img" aria-label="Kennel website screenshot" style="width:125px;background:linear-gradient(#c9b56a,#4d5a2a)"></div><h4>Maple Ridge Fire Department</h4><p>Web Design</p><a href="#">www.mapleridgefire.com</a></div>
  <div class="abs work" style="left:469px"><div class="thumb" role="img" aria-label="Real estate website screenshot" style="width:115px;background:linear-gradient(#b0202a,#1e3c68 40%,#101c30)"></div><h4>Maple Ridge Fire Department</h4><p>Web Design</p><a href="#">www.mapleridgefire.com</a></div>
  <div class="abs work" style="left:630px"><div class="thumb" role="img" aria-label="Landscaping website screenshot" style="width:155px;background:linear-gradient(#111,#3e5a2a 50%,#1a1a1a)"></div><h4>Maple Ridge Fire Department</h4><p>Web Design</p><a href="#">www.mapleridgefire.com</a></div>
</section>

<footer>
  <div class="abs footcol" style="left:153px"><h5>Home</h5><ul><li>About</li><li>Contact</li><li>Login</li></ul></div>
  <div class="abs footcol" style="left:260px"><h5>Search Engine Marketing</h5><ul><li>Local Map Listings</li><li>National SEO</li><li>Learn SEO</li></ul></div>
  <div class="abs footcol" style="left:405px"><h5>Website Design</h5><ul><li>Client Controlled Website</li><li>Flash Website</li><li>Build a Website that Sells</li></ul></div>
  <div class="abs footcol" style="left:526px"><h5>Graphic Design</h5><ul><li>Business Card Design</li><li>Logo Design</li><li>Flash Design</li></ul></div>
  <div class="abs widget">
    <div class="top"><i></i><b>BRIGHTLANE PIXEL COLLECTIVE</b></div>
    <div class="like">You and 692 others like Northwind Studio.</div>
    <div class="faces" role="img" aria-label="Member profile pictures"><i></i><i></i><i></i><i></i><i></i></div>
    <div class="plug">Social plugin</div>
  </div>
  <div class="abs social"><i style="background:#3b5ba0"></i><i style="background:#2ca7e0"></i><i style="background:#d42a1e"></i></div>
  <div class="abs foot-brand"><div class="brand-mark"></div><div class="brand-name">BRIGHTLANE PIXEL COLLECTIVE</div></div>
  <div class="abs legal"><span class="city">MINNEAPOLIS, MINNESOTA</span>Home | Privacy Policy | Refund Policy | Terms &amp; Conditions | About | Affiliates | Contact</div>
  <div class="abs copy">© 2009-2013 Brightlane Pixel Collective, Inc. All rights reserved.</div>
</footer>

</body>
</html>
```